Real Estate Sign Project

We need a Real Estate sign that promotes the property being listed and our company and agent listing the property. The images need to be able to be swapped out so we can use the template for each listing we have. I have a sample from another company that shows what were are trying to accomplish. Would want ours to be unique using our logo and the colors in our logo. We would like to not have to use a rider. Would want agents name and phone number to be part of the 36" x 24" sign.

Industry/Entity Type

Real Estate

Requirements
Must have
• Sign dimensions are 36 inches by 24 inches (36" across and 24" up down). Use example.of.sign.we.want.jpg as the direction we want to go but with a different layout and our logo and colors. This would be just a template that we can swap out new pictures, address, price, website, agents contact info for each home we are listing. Like the idea of the pictures bleeding off the sides. Please use free stock photos for the home images as we will be changing these out for each listing. Please incorporate all info including agents info into the one sign. File must be layered so we can change the pictures, price, website, agent, etc. We use GIMP (.xcf) file

```html
<!DOCTYPE html>
<html lang="en">
<head>
<meta charset="utf-8">
<title>Keystone Realty Group – Listing Sign</title>
<link rel="stylesheet" href="https://fonts.googleapis.com/css2?family=Questrial&family=Arimo:wght@700&display=swap">
<style>
  :root {
    --orange: #e3601f;
    --navy: #1e2f5a;
    --navy-deep: #172b4d;
    --blue: #1b7fc4;
    --blue-light: #2f8fd6;
    --white: #ffffff;
  }
  html, body {
    margin: 0;
    padding: 0;
    overflow: hidden;
    background: #ffffff;
  }
  .sign {
    position: relative;
    width: 1200px;
    height: 800px;
    overflow: hidden;
    background: var(--white);
    font-family: "Questrial", "Century Gothic", sans-serif;
    color: var(--navy);
  }
  .price-bar {
    position: absolute;
    left: 0; top: 0;
    width: 1200px; height: 146px;
    background: var(--orange);
    display: flex;
    align-items: center;
    justify-content: flex-end;
    padding-right: 44px;
    box-sizing: border-box;
    color: var(--white);
  }
  .price-bar .label {
    font-size: 34px;
    margin-right: 30px;
    margin-top: 22px;
  }
  .price-bar .price {
    font-family: "Arimo", Arial, sans-serif;
    font-weight: 700;
    font-size: 88px;
    letter-spacing: -1px;
  }
  .brand {
    position: absolute;
    left: 40px; top: 190px;
    width: 300px;
    text-align: center;
  }
  .brand .dot {
    width: 74px; height: 74px;
    border-radius: 50%;
    background: var(--orange);
    margin: 0 auto 22px;
  }
  .brand .name {
    font-size: 40px;
    line-height: 1.1;
    color: var(--navy);
  }
  .photo {
    position: absolute;
  }
  .photo-bedroom {
    left: 436px; top: 146px; width: 484px; height: 312px;
    background: linear-gradient(180deg, #8a8478 0%, #a59a88 40%, #8d7a63 70%, #5a4a3a 100%);
  }
  .photo-rail {
    position: absolute;
    left: 920px; top: 146px; width: 280px; height: 512px;
    background: var(--orange);
  }
  .rail-edge {
    position: absolute;
    left: 432px; top: 146px; width: 4px; height: 312px;
    background: var(--orange);
  }
  .photo-living {
    left: 928px; top: 146px; width: 272px; height: 150px;
    background: linear-gradient(160deg, #d9c6a4 0%, #a9784a 55%, #6b3f22 100%);
  }
  .photo-kitchen {
    left: 928px; top: 302px; width: 272px; height: 176px;
    background: linear-gradient(180deg, #c9a57a 0%, #b88c5c 50%, #8e6a46 100%);
  }
  .photo-exterior {
    left: 928px; top: 484px; width: 272px; height: 174px;
    background: linear-gradient(180deg, #4e86c8 0%, #a9c6e4 45%, #c7ccd0 62%, #5d8a3a 100%);
  }
  .address {
    position: absolute;
    left: 108px; top: 532px;
    width: 380px;
    font-size: 45px;
    white-space: nowrap;
    color: var(--navy);
  }
  .brace {
    position: absolute;
    left: 500px; top: 478px;
  }
  .features {
    position: absolute;
    left: 548px; top: 484px;
    margin: 0; padding: 0;
    list-style: none;
    font-size: 30px;
    line-height: 36.5px;
    color: var(--navy);
  }
  .web-band {
    position: absolute;
    left: 0; top: 658px;
    width: 1200px; height: 36px;
    background: var(--blue);
    color: var(--white);
    font-size: 21px;
    text-align: center;
    line-height: 36px;
  }
  .agent-bar {
    position: absolute;
    left: 0; top: 694px;
    width: 1200px; height: 106px;
    background: var(--navy-deep);
    color: var(--white);
  }
  .agent-bar .mark {
    position: absolute;
    left: 26px; top: 30px;
    width: 46px; height: 46px;
    border-radius: 50%;
    background: var(--orange);
  }
  .agent-bar .agent {
    position: absolute;
    left: 126px; top: 24px;
    font-family: "Arimo", Arial, sans-serif;
    font-weight: 700;
    font-size: 45px;
    white-space: nowrap;
  }
  .agent-bar .agent .role {
    color: var(--blue-light);
  }
  .agent-bar .phone {
    position: absolute;
    right: 50px; top: 22px;
    font-family: "Arimo", Arial, sans-serif;
    font-weight: 700;
    font-size: 48px;
  }
</style>
</head>
<body>
<div class="sign">
  <header class="price-bar">
    <span class="label">Home For Sale</span>
    <span class="price">$360,000</span>
  </header>

  <div class="brand">
    <div class="dot"></div>
    <div class="name">Keystone Realty Group</div>
  </div>

  <div class="rail-edge"></div>
  <div class="photo photo-bedroom" role="img" aria-label="Photo of the master bedroom with upholstered bed and pendant lamps"></div>
  <div class="photo-rail"></div>
  <div class="photo photo-living" role="img" aria-label="Photo of the living room with fireplace and hardwood floors"></div>
  <div class="photo photo-kitchen" role="img" aria-label="Photo of the kitchen with wood cabinets and granite island"></div>
  <div class="photo photo-exterior" role="img" aria-label="Photo of the two-storey house exterior with front lawn"></div>

  <div class="address">1427 Maple Road</div>
  <svg class="brace" width="40" height="166" viewBox="0 0 40 166" aria-hidden="true">
    <path d="M34 4 C18 4 18 10 18 24 L18 66 C18 78 14 83 4 83 C14 83 18 88 18 100 L18 142 C18 156 18 162 34 162"
          fill="none" stroke="#1e2f5a" stroke-width="3.5" stroke-linecap="round"/>
  </svg>
  <ul class="features">
    <li>4 Bedrooms</li>
    <li>3.5 Baths</li>
    <li>3200 Finished SF</li>
    <li>2-Car Garage</li>
  </ul>

  <div class="web-band">KeystoneRealtyGroup.com/1427Maple</div>

  <footer class="agent-bar">
    <div class="mark"></div>
    <div class="agent"><span class="role">AGENT:</span> John Doe</div>
    <div class="phone">xxx/xxx/xxxx</div>
  </footer>
</div>
</body>
</html>
```